Velvet Lantern rebranding my business with a new business card

I have my new logo and now I need a refresher on my business cards. I really want something fun and fresh. I like black background or anything to make the color pop.
Logo
Name: Velvet Lantern
Contact Info as stated below:
Mara Pelkin
519-555-0147
Logo
Name: Velvet Lantern
Mara Pelkin
519-555-0147
fb.me/VelvetLanternbyMara
Instagram: @VelvetLanternbyMara

Industry/Entity Type

Business

Contact Information for Business Card

double-sided. Logo on one side. Contact info on the other.

Requirements
Must have
• Logo
• Name: Velvet Lantern
• Contact Info as stated below:
• Mara Pelkin
• 519-555-0147
• fb.me/VelvetLanternbyMara
• fb.me/VelvetLanternbyMara

```html
<!DOCTYPE html>
<html lang="en">
<head>
<meta charset="utf-8">
<title>Velvet Lantern – Business Card</title>
<link href="https://fonts.googleapis.com/css2?family=Arimo:wght@400&family=Pinyon+Script&display=swap" rel="stylesheet">
<style>
  :root {
    --backdrop: #ece9e6;
    --pink-light: #fdf1f5;
    --pink-mid: #f5c4d4;
    --pink-edge: #eeaabf;
    --ring: #e58aa6;
    --ink: #2b2426;
    --red: #c62a30;
    --red-deep: #b32228;
    --white: #ffffff;
    --muted-blue: #3b5998;
  }
  * { box-sizing: border-box; margin: 0; padding: 0; }
  html, body {
    width: 1200px; height: 1200px; overflow: hidden;
    background: var(--backdrop);
  }
  .sheet {
    width: 1200px; height: 1200px;
    display: flex; flex-direction: column;
    align-items: center; justify-content: center; gap: 60px;
  }
  .card {
    position: relative;
    width: 900px; height: 514px;
    overflow: hidden;
    box-shadow: 0 6px 18px rgba(0,0,0,0.18);
  }

  /* Front: logo side */
  .card-front {
    background: radial-gradient(ellipse at 52% 48%, var(--pink-light) 0%, var(--pink-mid) 70%, var(--pink-edge) 100%);
    display: flex; align-items: center; justify-content: center;
  }
  .badge {
    width: 300px; height: 300px; border-radius: 50%;
    border: 3px solid var(--ring);
    box-shadow: 0 0 0 6px var(--pink-light), 0 0 0 8px var(--ring);
    background: var(--pink-light);
    display: flex; align-items: center; justify-content: center;
  }
  .badge-name {
    font-family: "Arimo", Arial, sans-serif;
    font-size: 30px; color: var(--red); letter-spacing: 1px;
    text-transform: uppercase;
  }

  /* Back: contact side */
  .card-back { background: var(--white); }
  .card-back .swoosh { position: absolute; inset: 0; }
  .brand-mark {
    position: absolute; left: 50px; top: 150px;
    width: 300px; height: 214px;
    display: flex; align-items: center; justify-content: center;
    font-family: "Arimo", Arial, sans-serif;
    font-size: 36px; color: var(--red); letter-spacing: 1px;
    text-transform: uppercase; text-align: center; line-height: 1.2;
  }
  .owner-name {
    position: absolute; right: 70px; top: 40px;
    font-family: "Pinyon Script", cursive;
    font-weight: 400;
    font-size: 60px; color: var(--white);
  }
  .contact {
    position: absolute; right: 40px; top: 262px;
    list-style: none;
    font-family: "Arimo", Arial, sans-serif;
    font-size: 20px; color: var(--white);
    text-align: right; line-height: 38px;
  }
  .contact li { display: flex; justify-content: flex-end; align-items: center; gap: 10px; white-space: nowrap; }
  .contact .icon { width: 24px; height: 24px; flex: none; }
  .contact .icon-blank { width: 24px; flex: none; }
  .social-square { width: 20px; height: 20px; background: var(--muted-blue); border-radius: 3px; margin: 0 2px; flex: none; }
</style>
</head>
<body>
<main class="sheet">

  <section class="card card-front" aria-label="Card front">
    <div class="badge">
      <span class="badge-name">Velvet Lantern</span>
    </div>
  </section>

  <section class="card card-back" aria-label="Card back">
    <svg class="swoosh" viewBox="0 0 900 514" width="900" height="514" aria-hidden="true">
      <path d="M330 0 Q 490 70 520 190 Q 430 70 310 0 Z" fill="var(--red)"/>
      <path d="M380 0 Q 600 170 540 514 L900 514 L900 0 Z" fill="var(--red)"/>
      <path d="M380 0 Q 600 170 540 514 L568 514 Q 620 170 405 0 Z" fill="var(--red-deep)" opacity="0.35"/>
    </svg>

    <div class="brand-mark">Velvet Lantern</div>

    <h1 class="owner-name">Mara Pelkin</h1>

    <ul class="contact">
      <li>VELVET LANTERN
        <svg class="icon" viewBox="0 0 26 26" aria-hidden="true">
          <path d="M3 9 Q13 1 23 9 L20 12 L17 9.5 L17 7.5 Q13 6 9 7.5 L9 9.5 L6 12 Z" fill="var(--white)"/>
          <path d="M7 13 L19 13 L22 22 L4 22 Z" fill="var(--white)"/>
          <circle cx="13" cy="17.5" r="2.4" fill="var(--red)"/>
        </svg>
      </li>
      <li>519-555-0147 <span class="social-square" aria-hidden="true"></span></li>
      <li>fb.me/VelvetLanternbyMara <span class="icon-blank"></span></li>
    </ul>
  </section>

</main>
</body>
</html>
```